Illustrationen für Versicherungsunternehmen
Zielgruppe
Versicherungsunternehmen. Zielgruppen sind sowohl Firmen als auch Privatpersonen in jeder Altersklasse.
Die hier adressierte Zielgruppe sind moderndenkende, kreative Mitarbeiter.
Aufgabenstellung
Es geht um die Visualisierung eines Team-Manifests bestehend aus 15 Prinzipien. Diese sollen möglichst ansprechend, kreativ, aber auch nicht zu verspielt dargestellt werden. Außerdem soll die Darstellung auch noch das bereits vorhandene Projektlogo (Anhang) enthalten, dieses soll auch nicht im Vordergrund/Fokus stehen.
Ein Beispiel für eine ähnliche Visualisierung ist im Anhang beigefügt, diese entspricht optisch sehr stark den Vorstellungen. Es soll am Ende eine Vorlage für ein Plakat entstehen, welches man in unterschiedlichen Formaten (DIN 4 bis DIN 0) erstellen kann. Bei der Farbgebung sollte die dominierende Farbe blau (Blautöne) sein, ergänzt durch orangefarbene Akzente. Die 15 Prinzipien sind der 2.Anlage zu entnehmen.

```html
<!DOCTYPE html>
<html lang="de">
<head>
<meta charset="utf-8">
<title>Team-Manifest</title>
<link rel="stylesheet" href="https://fonts.googleapis.com/css2?family=Bebas+Neue&family=Josefin+Sans:wght@300;400&family=Montserrat:wght@800;900&family=Alfa+Slab+One&family=Oswald:wght@300;600&display=swap">
<style>
  :root {
    --blue: #1f5ee8;
    --orange: #ff5a14;
    --paper: #ffffff;
  }
  * { margin: 0; padding: 0; box-sizing: border-box; }
  html, body { width: 849px; height: 1200px; overflow: hidden; background: var(--paper); }
  .poster { position: relative; width: 849px; height: 1200px; background: var(--paper); overflow: hidden; }
  .line { position: absolute; left: 26px; width: 799px; display: flex; justify-content: space-between; align-items: baseline; gap: 12px; white-space: nowrap; line-height: 1; color: var(--blue); }
  .blue { color: var(--blue); }
  .orange { color: var(--orange); }
  .thin { font-family: "Josefin Sans", sans-serif; font-weight: 300; }
  .light { font-family: "Josefin Sans", sans-serif; font-weight: 400; }
  .heavy { font-family: "Montserrat", sans-serif; font-weight: 900; }
  .cond { font-family: "Bebas Neue", sans-serif; font-weight: 400; }
  .ocond { font-family: "Oswald", sans-serif; font-weight: 300; }
  .slab { font-family: "Alfa Slab One", serif; font-weight: 400; }
  .bar { position: absolute; background: var(--blue); border-radius: 3px; }

  .brand { position: absolute; left: 26px; top: 300px; width: 481px; height: 145px; display: flex; align-items: center; gap: 18px; }
  .brand-mark { width: 34px; height: 34px; background: var(--blue); flex: none; }
  .brand-name { font-family: "Montserrat", sans-serif; font-weight: 800; font-size: 42px; color: var(--blue); white-space: nowrap; }
</style>
</head>
<body>
<main class="poster">
  <div class="line thin" style="top:19px;font-size:29px;letter-spacing:0.5px;"><span>WIR GESTALTEN <b class="heavy" style="font-size:26px">HEUTE</b> UND DENKEN AN MORGEN</span></div>

  <div class="line" style="top:66px;font-size:46px;"><span class="heavy" style="font-size:39px;letter-spacing:0.5px">UNSERE VORSORGE</span><span class="light">BRAUCHT</span></div>

  <div class="line light" style="top:120px;width:384px;font-size:42px;letter-spacing:2px;"><span>KEINEN LIKÖR</span></div>
  <div class="bar" style="left:26px;top:166px;width:384px;height:8px;"></div>
  <div class="line slab" style="top:128px;left:419px;width:406px;font-size:38px;letter-spacing:6px;"><span>TRAU´</span><span>DICH</span></div>

  <div class="line thin" style="top:186px;font-size:25px;"><span>DIE PROBLEME UNSERER KUNDEN SIND UNSERE PROBLEME</span></div>

  <div class="line heavy orange" style="top:236px;font-size:43px;"><span>VERTRAUEN UM ZU VERTRAUEN</span></div>

  <div class="brand"><span class="brand-mark"></span><span class="brand-name">Projekt Horizont</span></div>

  <div class="line heavy" style="top:302px;left:525px;width:300px;font-size:19px;"><span>WIR SPRECHEN KLARTEXT</span></div>
  <div class="line cond" style="top:350px;left:525px;width:300px;font-size:56px;"><span>VERSPROCHEN IST</span></div>
  <div class="line cond orange" style="top:404px;left:525px;width:300px;font-size:64px;"><span>VERSPROCHEN</span></div>

  <div class="line" style="top:484px;width:474px;font-size:60px;"><span class="cond orange">FAIR</span><span class="ocond">ODER GAR NICHT</span></div>
  <div class="line" style="top:551px;width:474px;font-size:58px;"><span class="ocond">DENKBAR IST</span><span class="cond orange">MACHBAR</span></div>
  <div class="line cond" style="top:484px;left:525px;width:300px;font-size:54px;"><span class="orange">GEMEINSAM</span><span>SIND</span></div>
  <div class="line cond" style="top:540px;left:525px;width:300px;font-size:72px;"><span>WIR STÄRKER</span></div>

  <div class="line heavy" style="top:627px;font-size:37px;"><span>WIR SIND ENTSCHEIDUNGSFREUDIG</span></div>

  <div class="bar" style="left:26px;top:691px;width:234px;height:20px;"></div>
  <div class="line light" style="top:689px;left:274px;width:551px;font-size:26px;letter-spacing:10px;"><span>JEDES ARGUMENT ZÄHLT</span></div>

  <div class="line thin" style="top:734px;font-size:40px;letter-spacing:1px;"><span>FEHLER MACHEN IST</span><span class="orange">KEIN FEHLER</span></div>

  <div class="line cond" style="top:799px;width:398px;font-size:48px;"><span>DENKVERBOTE SIND TABU</span></div>
  <div class="line thin" style="top:799px;left:450px;width:375px;font-size:46px;letter-spacing:4px;"><span>TRAU´</span><span>DICH</span></div>

  <div class="line cond" style="top:856px;font-size:84px;letter-spacing:3px;"><span>WIR SPRECHEN</span><span class="orange">KLARTEXT</span></div>

  <div class="line thin" style="top:944px;width:521px;font-size:50px;"><span>VERSPROCHEN IST</span></div>
  <div class="line thin orange" style="top:994px;width:521px;font-size:64px;"><span>VERSPROCHEN</span></div>
  <div class="line thin" style="top:946px;left:571px;width:254px;font-size:31px;"><span>DENKBAR IST</span></div>
  <div class="line thin orange" style="top:980px;left:571px;width:254px;font-size:34px;justify-content:center;"><span>MACHBAR</span></div>
  <div class="bar" style="left:571px;top:1035px;width:93px;height:22px;"></div>
  <div class="bar" style="left:682px;top:1035px;width:143px;height:22px;"></div>

  <div class="line cond orange" style="top:1084px;font-size:42px;"><span>FAIR <span class="ocond">ODER GAR NICHT</span></span><span>GEMEINSAM <span class="blue">SIND WIR</span> STÄRKER</span></div>

  <div class="line thin" style="top:1142px;font-size:37px;letter-spacing:1px;"><span>WIR HABEN OFFENE OHREN FÜR NEUES</span></div>
</main>
</body>
</html>
```